3 pages of UI design for AdTech Startup

We need 3 pages of UI design for a new AdTech company located in Seattle called KELVRA Systems.

We put digital, mobile billboards on college campuses throughout the country. This design project involves our back-end customer dashboard.

Page 1- Dashboard home page
page 2- Manage ads screen (see File 3 below for the screenshot of our current design). Please match the design of all 3 screens so there is consistency
page 3-Detailed Zone screen (see file 16 below). This page looks similar to the first page but gives a more detailed overview and a larger map.

The features and functionality are already built but we are lacking an aesthetically pleasing and slick design. Looking for someone who can match our website look to this new dashboard space. Our company reflects modern, clean, elegant design that is straight-forward and user friendly (main inspiration is TROVI, we love their design and feel).

Target Market(s)

-Local business owner, marketing directors, and national advertising and marketing agencies

Industry/Entity Type

Advertising

Number of Pages Required

3 page

Font styles to use
Other font styles liked:
• Proxima Nova- Thin for body text, Light for title

Colors
85cae6
33a6d7
0292cd
ffffff

Requirements
Nice to have
• Please include enough detail so that my developer can look at the design you come up with and translate it to html. Please include spacing, fonts, color numbers. My developer is going to look at your creation and recreate it in html format

```html
<!DOCTYPE html>
<html lang="en">
<head>
<meta charset="utf-8">
<title>KELVRA Dashboard</title>
<link href="https://fonts.googleapis.com/css2?family=Roboto:wght@300;400;500&family=Roboto+Condensed:wght@300;400&display=swap" rel="stylesheet">
<style>
  :root{
    --sky:#85cae6;
    --blue:#33a6d7;
    --blue-bright:#3bb4e5;
    --blue-deep:#0292cd;
    --white:#ffffff;
    --ink:#333333;
    --text:#555555;
    --muted:#666666;
    --dark:#30303b;
    --rule:#3b3b47;
    --band:#eeeeee;
    --page:#f3f3f3;
    --line:#e4e4e4;
  }
  *{box-sizing:border-box;margin:0;padding:0}
  html,body{width:1200px;height:1101px;overflow:hidden}
  body{position:relative;background:var(--page);font-family:"Roboto",sans-serif;color:var(--text)}

  .sidebar{position:absolute;left:0;top:0;width:269px;height:996px;background:var(--dark)}
  .brand{height:171px;background:var(--white);display:flex;flex-direction:column;align-items:center;justify-content:center;gap:10px}
  .brand-dot{width:54px;height:54px;border-radius:50%;background:var(--blue-bright)}
  .brand-name{font-family:"Roboto",sans-serif;font-weight:300;font-size:32px;letter-spacing:1px;color:var(--ink)}
  .nav-item{display:flex;align-items:center;height:48px;border-bottom:1px solid var(--rule);color:var(--white);font-size:15.5px;font-weight:400;position:relative}
  .nav-item.active{height:57px;background:var(--blue-bright);border-bottom:none}
  .nav-icon{width:68px;height:100%;display:flex;align-items:center;justify-content:center}
  .nav-item.active .nav-icon{background:var(--blue)}
  .nav-label{padding-left:14px}
  .nav-chevron{position:absolute;right:18px;top:50%;transform:translateY(-50%)}

  .topbar{position:absolute;left:269px;top:0;width:931px;height:88px;background:var(--white)}
  .account{position:absolute;left:960px;top:24px;display:flex;align-items:center}
  .client-dot{width:38px;height:38px;border-radius:50%;background:#1e6b45}
  .client-meta{margin-left:11px;line-height:1.45}
  .client-name{font-size:11px;color:var(--muted);letter-spacing:.3px}
  .client-user{font-size:12.5px;color:var(--muted)}
  .logout{position:absolute;left:1102px;top:30px;width:65px;height:26px;border:1px solid var(--blue);border-radius:3px;color:var(--blue);font-size:12.5px;display:flex;align-items:center;justify-content:center}

  .title-band{position:absolute;left:269px;top:88px;width:931px;height:67px;background:var(--band)}
  .page-title{position:absolute;left:23px;top:18px;font-family:"Roboto Condensed",sans-serif;font-weight:400;font-size:26px;color:var(--ink)}
  .accent{color:var(--blue-bright)}

  .card{position:absolute;background:var(--white);border:1px solid #e8e8e8}
  .chart-card{left:304px;top:194px;width:862px;height:416px}
  .card-title{position:absolute;left:66px;top:33px;font-family:"Roboto Condensed",sans-serif;font-size:20px;color:var(--ink)}
  .range{position:absolute;left:396px;top:33px;display:flex;border:1px solid #c9c9c9;border-radius:2px;overflow:hidden}
  .range span{height:23px;display:flex;align-items:center;justify-content:center;font-size:11.5px;color:var(--muted);border-right:1px solid #c9c9c9;background:#f6f6f6}
  .range span:last-child{border-right:none}
  .range .on{background:#e2e2e2}
  .date{position:absolute;top:33px;height:25px;width:104px;border:1px solid #dcdcdc;display:flex;align-items:center;font-size:11px;color:var(--muted)}
  .date em{font-style:normal;padding-left:11px;flex:1}
  .date i{width:24px;height:100%;border-left:1px solid #dcdcdc;background:#f0f0f0;display:flex;align-items:center;justify-content:center}
  .date-to{position:absolute;left:675px;top:39px;font-size:11px;color:var(--ink)}
  .stats{position:absolute;left:690px;top:85px;list-style:none;font-size:13px;color:var(--text);line-height:25.7px}
  .plot{position:absolute;left:0;top:0}

  .zone-table{left:304px;top:644px;width:862px;height:316px}
  .zone-head{display:flex;height:51px;background:var(--blue-bright);color:var(--white);font-family:"Roboto Condensed",sans-serif;font-size:16.5px}
  .zone-head div{display:flex;align-items:center;justify-content:center;border-right:1px solid rgba(255,255,255,.35)}
  .zone-head div:last-child{border-right:none}
  .col-zone{width:151px}.col-ad{width:189px}.col-path{width:328px}.col-perf{width:194px}
  .zone-head .col-zone{justify-content:flex-start;padding-left:29px}
  .divider{position:absolute;top:51px;bottom:0;width:1px;background:#eeeeee}
  .zone-name{position:absolute;left:29px;top:72px;font-size:12.5px;color:var(--muted);line-height:20.5px}
  .ad-media{position:absolute;left:165px;top:73px;width:160px;height:161px;background:linear-gradient(180deg,#c0456a 0%,#2c5d96 35%,#0f2a4a 70%,#070d1a 100%)}
  .path-map{position:absolute;left:357px;top:72px;width:295px;height:204px;background:linear-gradient(135deg,#5f6d57 0%,#6b7a5c 35%,#847b6a 60%,#5e6275 100%)}
  .btn{position:absolute;height:29px;border-radius:2px;background:var(--blue-bright);color:var(--white);font-size:14px;display:flex;align-items:center;justify-content:center}
  .btn-manage{left:165px;top:246px;width:83px}
  .btn-details{left:689px;top:246px;width:83px}
  .perf{position:absolute;left:688px;top:74px;width:160px;font-size:12.3px;color:var(--muted)}
  .perf p{margin-bottom:10.5px}
  .perf .blurb{font-size:11.3px;line-height:20.6px;margin-top:6px}

  .footer{position:absolute;left:0;top:996px;width:1200px;height:105px;background:var(--dark)}
  .copyright{position:absolute;left:0;right:0;top:28px;text-align:center;font-size:11.5px;color:var(--white);font-weight:400}
  .social{position:absolute;top:56px;left:671px;display:flex;gap:4.5px}
  .social span{width:24px;height:24px;border:1.5px solid var(--white);border-radius:50%}
</style>
</head>
<body>

<aside class="sidebar">
  <div class="brand">
    <div class="brand-dot"></div>
    <div class="brand-name">KELVRA</div>
  </div>
  <nav>
    <div class="nav-item active">
      <div class="nav-icon">
        <svg width="20" height="18" viewBox="0 0 20 18"><path d="M10 1 L19 9 H16 V17 H12 V12 H8 V17 H4 V9 H1 Z" fill="#fff"/></svg>
      </div>
      <span class="nav-label">Dashboard</span>
      <svg class="nav-chevron" width="8" height="13" viewBox="0 0 8 13"><path d="M1 1 L6.5 6.5 L1 12" stroke="#fff" stroke-width="1.8" fill="none"/></svg>
    </div>
    <div class="nav-item">
      <div class="nav-icon">
        <svg width="24" height="20" viewBox="0 0 24 20"><g fill="#fff"><rect x="7" y="1" width="10" height="8" rx="1"/><rect x="1" y="11" width="10" height="8" rx="1"/><rect x="13" y="11" width="10" height="8" rx="1"/></g></svg>
      </div>
      <span class="nav-label">Resources</span>
      <svg class="nav-chevron" width="8" height="13" viewBox="0 0 8 13"><path d="M1 1 L6.5 6.5 L1 12" stroke="#fff" stroke-width="1.8" fill="none"/></svg>
    </div>
    <div class="nav-item">
      <div class="nav-icon">
        <svg width="18" height="20" viewBox="0 0 18 20"><g fill="#fff"><circle cx="9" cy="5.5" r="4.5"/><path d="M1 19 C1 12 17 12 17 19 Z"/></g></svg>
      </div>
      <span class="nav-label">My Profile</span>
      <svg class="nav-chevron" width="8" height="13" viewBox="0 0 8 13"><path d="M1 1 L6.5 6.5 L1 12" stroke="#fff" stroke-width="1.8" fill="none"/></svg>
    </div>
  </nav>
</aside>

<header class="topbar"></header>
<div class="account">
  <div class="client-dot"></div>
  <div class="client-meta">
    <div class="client-name">BRINDLE ROAST</div>
    <div class="client-user">Mara Quill</div>
  </div>
</div>
<div class="logout">Log Out</div>

<div class="title-band">
  <h1 class="page-title">KELVRA <span class="accent">DASHBOARD</span></h1>
</div>

<section class="card chart-card">
  <svg class="plot" width="862" height="416" viewBox="355 226 1006 486">
    <defs>
      <linearGradient id="areaFill" x1="0" y1="0" x2="0" y2="1">
        <stop offset="0" stop-color="#7fc9ec"/>
        <stop offset="1" stop-color="#a3daf3"/>
      </linearGradient>
    </defs>
    <g fill="#f7f7f7">
      <rect x="432" y="328" width="76" height="300"/>
      <rect x="584" y="328" width="76" height="300"/>
      <rect x="736" y="328" width="76" height="300"/>
      <rect x="888" y="328" width="76" height="300"/>
      <rect x="1040" y="328" width="75" height="300"/>
    </g>
    <g stroke="#dddddd" stroke-width="1">
      <line x1="432" y1="328" x2="1115" y2="328"/>
      <line x1="432" y1="378" x2="1115" y2="378"/>
      <line x1="432" y1="428" x2="1115" y2="428"/>
      <line x1="432" y1="478" x2="1115" y2="478"/>
      <line x1="432" y1="528" x2="1115" y2="528"/>
      <line x1="432" y1="578" x2="1115" y2="578"/>
    </g>
    <path d="M434 504 L528 539 L627 480 L727 516 L820 534 L919 501 L1017 489 L1111 436 L1115 436 L1115 628 L434 628 Z" fill="url(#areaFill)"/>
    <polyline points="434,504 528,539 627,480 727,516 820,534 919,501 1017,489 1111,436" fill="none" stroke="#2ba3d4" stroke-width="2"/>
    <g fill="#1f98c9">
      <circle cx="434" cy="504" r="4.5"/><circle cx="528" cy="539" r="4.5"/><circle cx="627" cy="480" r="4.5"/><circle cx="727" cy="516" r="4.5"/>
      <circle cx="820" cy="534" r="4.5"/><circle cx="919" cy="501" r="4.5"/><circle cx="1017" cy="489" r="4.5"/><circle cx="1111" cy="436" r="4.5"/>
    </g>
    <line x1="432" y1="328" x2="432" y2="634" stroke="#33a6d7" stroke-width="2"/>
    <line x1="432" y1="628" x2="1115" y2="628" stroke="#33a6d7" stroke-width="2"/>
    <g stroke="#33a6d7" stroke-width="1.5">
      <line x1="528" y1="628" x2="528" y2="634"/><line x1="627" y1="628" x2="627" y2="634"/><line x1="727" y1="628" x2="727" y2="634"/><line x1="820" y1="628" x2="820" y2="634"/><line x1="919" y1="628" x2="919" y2="634"/><line x1="1017" y1="628" x2="1017" y2="634"/><line x1="1114" y1="628" x2="1114" y2="634"/>
    </g>
    <g>
      <rect x="618" y="434" width="44" height="26" rx="13" fill="#52bde9"/>
      <path d="M632 458 L636 468 L642 458 Z" fill="#52bde9"/>
      <text x="640" y="452" text-anchor="middle" font-family="Roboto, sans-serif" font-size="12" fill="#fff">14.9K</text>
    </g>
    <g font-family="Roboto, sans-serif" font-size="13" fill="#333" text-anchor="end">
      <text x="419" y="432">20K</text><text x="419" y="482">15K</text><text x="419" y="532">10K</text><text x="419" y="582">5K</text><text x="419" y="632">0</text>
    </g>
    <g font-family="Roboto, sans-serif" font-size="12.5" fill="#333" text-anchor="middle">
      <text x="452" y="657">Jul 29,</text><text x="447" y="672">2016</text>
      <text x="542" y="657">Jul 30,</text><text x="537" y="672">2016</text>
      <text x="630" y="657">Jul 31,</text><text x="625" y="672">2016</text>
      <text x="728" y="657">Aug 1,</text><text x="724" y="672">2016</text>
      <text x="825" y="657">Aug 2,</text><text x="821" y="672">2016</text>
      <text x="924" y="657">Aug 3,</text><text x="920" y="672">2016</text>
      <text x="1019" y="657">Aug 4,</text><text x="1015" y="672">2016</text>
      <text x="1105" y="657">Aug 5,</text><text x="1101" y="672">2016</text>
    </g>
  </svg>

  <h2 class="card-title">AREA <span class="accent">CHART</span></h2>
  <div class="range">
    <span class="on" style="width:52px">Day</span>
    <span style="width:51px">Week</span>
    <span style="width:51px">Month</span>
  </div>
  <div class="date" style="left:567px"><em>12-08-2014</em><i><svg width="9" height="9" viewBox="0 0 9 9"><rect x="0.5" y="1" width="8" height="7.5" fill="none" stroke="#555"/><rect x="0.5" y="1" width="8" height="2" fill="#555"/></svg></i></div>
  <span class="date-to">to</span>
  <div class="date" style="left:692px"><em>12-08-2014</em><i><svg width="9" height="9" viewBox="0 0 9 9"><rect x="0.5" y="1" width="8" height="7.5" fill="none" stroke="#555"/><rect x="0.5" y="1" width="8" height="2" fill="#555"/></svg></i></div>

  <ul class="stats">
    <li>Rotations:&nbsp; 85</li>
    <li>Time: 21.25 min</li>
    <li>Miles: 0.3 miles</li>
    <li>Impressions: 595</li>
    <li>Miles: 0.3 miles</li>
  </ul>
</section>

<section class="card zone-table">
  <div class="zone-head">
    <div class="col-zone">Zone</div>
    <div class="col-ad">Active Ad</div>
    <div class="col-path">Carrier Paths</div>
    <div class="col-perf">Zone Performance</div>
  </div>
  <span class="divider" style="left:151px"></span>
  <span class="divider" style="left:340px"></span>
  <span class="divider" style="left:668px"></span>

  <div class="zone-name">Zone 1<br>Lena's House</div>
  <div class="ad-media" role="img" aria-label="Active ad photo: concert crowd under stage lights"></div>
  <div class="btn btn-manage">Manage</div>
  <div class="path-map" role="img" aria-label="Aerial map of the zone with carrier paths"></div>
  <div class="perf">
    <p>Rotations:&nbsp; 85</p>
    <p>Broadcast Time: 21.25 min</p>
    <p>Miles: 0.3 miles</p>
    <div class="blurb">Sed ut perspiciatis unde omnis iste natus error sit voluptatem accusantium doloremque lau-dantium, totam rem</div>
  </div>
  <div class="btn btn-details">Details</div>
</section>

<footer class="footer">
  <div class="copyright">©2016 KELVRA ., ALL RIGHTS RESERVED.</div>
  <div class="social"><span></span><span></span><span></span><span></span><span></span></div>
</footer>

</body>
</html>
```